A r&b and house DJ needs a new Graphically pleasing and trendy website for fans and potential client

Want a new design for a dj website. This website wont be updated often so needs to look very graphically pleasing and just be a point of call where fans and potential clients can come and see information about the dj etc.

Needs to have short bio , social network links, and a enquiry button.

You can use some stock images for the moment as some professional images are going to be taken.

Others DJ websites:

https://www.djvorrelan.com/
http://www.pelicorvane.com/
http://quibon.com/
http://umerko.com/
http://www.dorianpuckett.co.uk/gb/home
http://www.florvimmel.com/
http://pranelo.nl/

LOGO LINK IS HERE

https://www.filecrate.example/s/k7wmq3zr9xn2vle/DJ_Wembo_logo.eps?dl=0

Target Market(s)

Fans and also prospective clients ( Nightclubs, Record Labels)

Industry/Entity Type

House

Font styles to use
Sans Serif

Requirements
Must have
• Small Bio, Social Network Links, Enquiry Button.
Nice to have
• Social network links

```html
<!DOCTYPE html>
<html lang="en">
<head>
<meta charset="utf-8">
<title>DJ Wembo</title>
<link href="https://fonts.googleapis.com/css2?family=Questrial&display=swap" rel="stylesheet">
<style>
  :root {
    --red: #e0504f;
    --red-soft: rgba(222, 86, 84, 0.72);
    --black: #050505;
    --dark: #121212;
    --panel-line: #2a2a2a;
    --muted: #4a4a4a;
    --white: #ffffff;
    --icon: #3c3c3c;
  }
  * { box-sizing: border-box; margin: 0; padding: 0; }
  html, body { width: 900px; height: 1200px; overflow: hidden; }
  body {
    position: relative;
    background: var(--dark);
    font-family: "Questrial", Arial, sans-serif;
    color: var(--white);
  }
  .site-header {
    position: absolute; left: 0; top: 0; width: 900px; height: 70px;
    background: var(--black);
  }
  .brand {
    position: absolute; left: 73px; top: 21px;
    font-size: 24px; line-height: 28px; color: var(--white);
  }
  .main-nav {
    position: absolute; left: 390px; top: 29px;
    display: flex; gap: 20px; font-size: 12px; line-height: 14px;
  }
  .main-nav a { color: var(--white); text-decoration: none; }
  .main-nav a.is-active { color: var(--red); }
  .social-links {
    position: absolute; left: 712px; top: 26px; display: flex; gap: 9px;
  }
  .social-links span {
    width: 20px; height: 20px; border-radius: 50%; background: var(--icon);
  }
  .social-links span.is-primary { background: var(--red); }

  .hero {
    position: absolute; left: 0; top: 70px; width: 900px; height: 542px;
    background:
      radial-gradient(ellipse 220px 260px at 400px 150px, rgba(214,170,120,0.55), transparent 70%),
      radial-gradient(ellipse 300px 180px at 720px 180px, rgba(140,60,110,0.55), transparent 70%),
      radial-gradient(ellipse 260px 200px at 120px 200px, rgba(110,60,80,0.5), transparent 70%),
      linear-gradient(180deg, #3a2530 0%, #2a1c28 55%, #151015 100%);
  }
  .booking-panel {
    position: absolute; left: 127px; top: 323px; width: 648px; height: 287px;
    background: var(--red-soft);
  }
  .panel-title {
    position: absolute; font-size: 18px; font-weight: 400; color: var(--white);
    padding-bottom: 8px; border-bottom: 1px solid rgba(255,255,255,0.8);
  }
  .book-title { left: 21px; top: 42px; width: 129px; }
  .welcome-title { left: 240px; top: 42px; width: 128px; }
  .field {
    position: absolute; left: 23px; width: 176px; height: 32px;
    border: 1px solid rgba(255,255,255,0.45); border-radius: 3px;
    background: rgba(255,255,255,0.12);
    font-size: 10px; padding: 10px 11px; color: var(--white);
  }
  .field-name { top: 89px; }
  .field-email { top: 132px; }
  .book-note {
    position: absolute; left: 23px; top: 174px; width: 180px;
    font-size: 10px; line-height: 16px;
  }
  .send-button {
    position: absolute; left: 23px; top: 212px; width: 176px; height: 30px;
    background: var(--white); border-radius: 3px; color: var(--red);
    font-size: 11px; text-align: center; line-height: 30px;
  }
  .welcome-media {
    position: absolute; left: 243px; top: 92px; width: 202px; height: 148px;
    border: 2px solid #e06a66; border-radius: 4px;
    background: radial-gradient(ellipse at 60% 35%, #8a8a90, #2a2a2e 60%, #0b0b0d);
  }
  .welcome-text {
    position: absolute; left: 458px; top: 88px; width: 180px;
    font-size: 10px; line-height: 16px;
  }

  .gallery {
    position: absolute; left: 75px; top: 687px; display: flex; gap: 17px;
  }
  .gallery-item { width: 239px; height: 128px; border: 2px solid #2e2e2e; }
  .gallery-item.one { background: linear-gradient(120deg, #7a2f9a, #2a3ab0 55%, #c23a7a); }
  .gallery-item.two { background: linear-gradient(180deg, #3a4f9a, #7a3a9a 55%, #2a1a3a); }
  .gallery-item.three { background: radial-gradient(ellipse at 50% 30%, #3a4acc, #141a40 60%, #05060f); }

  .section-title {
    position: absolute; top: 882px; font-size: 14px; font-weight: 400; color: var(--red);
  }
  .categories-title { left: 73px; }
  .about-title { left: 223px; }
  .news-title { left: 540px; }
  .category-list {
    position: absolute; left: 73px; top: 912px; list-style: none;
    font-size: 10px; line-height: 26.8px; color: var(--muted);
  }
  .category-list li.is-active { color: var(--red); }
  .about-card {
    position: absolute; left: 224px; top: 915px; width: 267px; height: 142px;
    border: 2px solid var(--panel-line); background: #161616;
  }
  .about-photo {
    position: absolute; left: 0; top: 0; width: 140px; height: 138px;
    background: linear-gradient(150deg, #3a5a8a, #2a1a2a 55%, #8a2020);
  }
  .about-text {
    position: absolute; left: 151px; top: 17px; width: 105px;
    font-size: 10px; line-height: 17.5px; color: var(--muted);
  }
  .news-item { position: absolute; left: 541px; width: 290px; height: 68px; }
  .news-item.first { top: 915px; }
  .news-item.second { top: 998px; }
  .news-thumb {
    position: absolute; left: 0; top: 0; width: 68px; height: 68px;
    border: 2px solid #333;
    background: linear-gradient(135deg, #c8702a, #3a6ab0 60%, #1a2a4a);
  }
  .news-text {
    position: absolute; left: 85px; top: 2px; width: 205px;
    font-size: 10px; line-height: 16px; color: var(--muted);
  }
  .news-date {
    position: absolute; left: 85px; top: 55px; font-size: 9px; color: var(--red);
  }

  .site-footer {
    position: absolute; left: 0; top: 1135px; width: 900px; height: 65px;
    background: var(--red); text-align: center; line-height: 65px;
    font-size: 11px; color: var(--white);
  }
</style>
</head>
<body>
  <header class="site-header">
    <div class="brand">DJ Wembo</div>
    <nav class="main-nav">
      <a class="is-active" href="#">Home</a>
      <a href="#">MP3</a>
      <a href="#">Videos</a>
      <a href="#">Night Club</a>
      <a href="#">Contact Us</a>
    </nav>
    <div class="social-links" aria-label="Social network links">
      <span class="is-primary"></span><span></span><span></span><span></span>
    </div>
  </header>

  <section class="hero" role="img" aria-label="Photo of a female DJ wearing headphones against blurred club lights"></section>

  <section class="booking-panel">
    <h2 class="panel-title book-title">Book Your DJ</h2>
    <div class="field field-name">Name</div>
    <div class="field field-email">Email</div>
    <p class="book-note">Lorem ipsum dolor sit amet, consectetuer adipiscing elit..</p>
    <div class="send-button">Send</div>

    <h2 class="panel-title welcome-title">Welcome To Dj</h2>
    <div class="welcome-media" role="img" aria-label="Photo of a DJ playing at a mixing desk"></div>
    <p class="welcome-text">Lorem ipsum dolor sit amet, consectetuer adipiscing elit, sed diam nonummy nibh euismod tincidunt ut laoreet dolore magna aliquam erat volutpat. Ut wisi enim ad minim veniam, quis nostrud exerci tation ullamcorper suscipit lobortis nisl ut aliquip ex ea commodo consequat.</p>
  </section>

  <div class="gallery">
    <div class="gallery-item one" role="img" aria-label="Photo of a DJ with light trails at the decks"></div>
    <div class="gallery-item two" role="img" aria-label="Photo of a DJ performing to a large crowd"></div>
    <div class="gallery-item three" role="img" aria-label="Photo of a DJ behind lit turntables"></div>
  </div>

  <h3 class="section-title categories-title">Categories</h3>
  <ul class="category-list">
    <li class="is-active">Music</li>
    <li>Music Instruments</li>
    <li>Electronics</li>
    <li>Movies</li>
    <li>Dj</li>
    <li>Lcd Panels</li>
  </ul>

  <h3 class="section-title about-title">Who I Am</h3>
  <div class="about-card">
    <div class="about-photo" role="img" aria-label="Photo of the DJ with a vinyl record"></div>
    <p class="about-text">Lorem ipsum dolor sit amet, consectetuer adipiscing elit, sed diam nonummy nibh euismod tincidunt ut laoreet dolore</p>
  </div>

  <h3 class="section-title news-title">News &amp; Events</h3>
  <article class="news-item first">
    <div class="news-thumb" role="img" aria-label="Event thumbnail of a DJ at the decks"></div>
    <p class="news-text">Lorem ipsum dolor sit amet, consectetuer adipiscing elit, sed diam nonummy nibh euismod tincidunt ut laoreet dolore</p>
    <span class="news-date">14 . feb . 2015</span>
  </article>
  <article class="news-item second">
    <div class="news-thumb" role="img" aria-label="Event thumbnail of a DJ at the decks"></div>
    <p class="news-text">Lorem ipsum dolor sit amet, consectetuer adipiscing elit, sed diam nonummy nibh euismod tincidunt ut laoreet dolore</p>
    <span class="news-date">14 . feb . 2015</span>
  </article>

  <footer class="site-footer">Copyright © 2015 DJ Wembo</footer>
</body>
</html>
```